Anzeigengestaltung für Reinigungsunternehmen
Zielgruppe
Wir sind ein Reinigungsunternehmen mit den Haupttätigkeitsfeldern: Büroreinigung, Treppenhausreinigung und Bauendreinigung.
Webseite: www.lorvapur.de
Die Zielgruppe sind Unternehmer (überwiegend Büros), Hausverwaltungen sowie Bauherren.
Aufgabenstellung
Die Reinigungsfirma wird mit dieser Anzeige zum ersten Mal beworben.
Umkreis: Kreis Paderborn und Kreis Gütersloh
Die Anzeige soll sowohl in Facebook beworben werden, sowie auch in den örtlichen Rundschauen.

```html
<!DOCTYPE html>
<html lang="de">
<head>
<meta charset="utf-8">
<title>Lorvapur – Anzeigen</title>
<link href="https://fonts.googleapis.com/css2?family=Montserrat:wght@400;500;700;800&display=swap" rel="stylesheet">
<style>
  :root{
    --stage:#d2d2d1;
    --white:#ffffff;
    --brand-dark:#0a67aa;
    --brand-light:#0099d4;
    --navy:#1d4a7a;
    --photo-a:#c9d3dc;
    --photo-b:#6e7f90;
  }
  *{margin:0;padding:0;box-sizing:border-box}
  html,body{width:1200px;height:1101px;overflow:hidden}
  body{background:var(--stage);font-family:"Montserrat",sans-serif;position:relative}
  .ad{position:absolute;box-shadow:0 6px 18px rgba(0,0,0,.18);overflow:hidden}
  .ad svg.bg{position:absolute;left:0;top:0}
  .t{position:absolute;white-space:nowrap}
  .center{text-align:center;transform:translateX(-50%)}

  /* Skyscraper */
  .sky{left:180px;top:167px;width:135px;height:766px}
  .sky .brand{left:18px;top:22px;display:flex;align-items:center;gap:6px;color:var(--brand-dark);font-weight:800;font-size:17px}
  .sky .brand i{width:12px;height:12px;background:var(--brand-dark);display:block}
  .sky .owner{left:36px;top:46px;font-size:6px;color:var(--brand-dark)}
  .sky .headline{left:67px;top:92px;color:var(--white);font-size:13.5px;line-height:15.6px;font-weight:500}
  .sky .headline b{font-weight:800}
  .sky .lead{left:67px;top:182px;color:var(--white);font-size:8.5px;line-height:11.7px}
  .sky .offers-title{left:67px;top:271px;color:var(--white);font-size:13px;line-height:15.6px;font-weight:800}
  .sky .label{position:absolute;left:20px;width:94px;background:var(--brand-dark);color:var(--white);font-weight:700;font-size:8.5px;line-height:10px;text-align:center;display:flex;align-items:center;justify-content:center}
  .sky .cta{left:67px;top:700px;color:var(--white);font-weight:800;font-size:13px;line-height:16.5px}
  .sky .web{left:67px;top:736px;color:var(--white);font-weight:700;font-size:10px}

  /* Landscape */
  .wide{left:409px;top:370px;width:688px;height:361px}
  .wide .brand{left:33px;top:32px;display:flex;align-items:center;gap:10px;color:var(--brand-dark);font-weight:800;font-size:30px}
  .wide .brand i{width:20px;height:20px;background:var(--brand-dark);display:block}
  .wide .owner{left:63px;top:72px;font-size:8px;color:var(--brand-dark)}
  .wide .headline{left:27px;top:108px;color:var(--brand-dark);font-size:25.5px;line-height:30px;font-weight:800}
  .wide .headline span{color:var(--brand-light)}
  .wide .rule{position:absolute;left:29px;top:210px;width:74px;height:3px;background:var(--brand-dark)}
  .wide .lead{left:28px;top:230px;color:var(--brand-dark);font-size:17.5px;line-height:24px;font-weight:500}
  .wide .offers-title{left:489px;top:20px;color:var(--white);font-size:24px;font-weight:800}
  .wide .label{color:var(--white);font-size:12px;line-height:19px;font-weight:700}
  .wide .band{top:333px;color:var(--white);font-size:15.5px;font-weight:800}
  .wide .band.web{font-weight:700;font-size:15.5px}
</style>
</head>
<body>

<section class="ad sky" aria-label="Anzeige Hochformat">
  <svg class="bg" width="135" height="766" viewBox="0 0 135 766">
    <defs>
      <linearGradient id="photoTone" x1="0" y1="0" x2="0" y2="1">
        <stop offset="0" stop-color="var(--photo-a)"/>
        <stop offset="1" stop-color="var(--photo-b)"/>
      </linearGradient>
    </defs>
    <rect width="135" height="766" fill="var(--brand-light)"/>
    <polygon points="0,0 135,0 135,67 0,80" fill="var(--white)"/>
    <polygon points="0,80 135,67 135,254 0,268" fill="var(--brand-dark)"/>
    <rect x="55" y="249" width="26" height="2" fill="var(--white)"/>
    <g stroke="var(--white)" stroke-width="3">
      <polygon points="26,314 99,306 92,427 45,427" fill="url(#photoTone)" role="img" aria-label="Foto: Reinigungskraft wischt Büroboden"/>
      <polygon points="42,437 89,437 101,551 35,558" fill="url(#photoTone)" role="img" aria-label="Foto: Putzwagen mit Eimer im Treppenhaus"/>
      <polygon points="26,567 99,561 92,681 45,681" fill="url(#photoTone)" role="img" aria-label="Foto: Poliermaschine auf glänzendem Boden"/>
    </g>
    <rect x="0" y="690" width="135" height="76" fill="var(--brand-dark)"/>
  </svg>
  <div class="t brand"><i></i>Lorvapur</div>
  <div class="t owner">Inh. Jonas Merbeck</div>
  <div class="t center headline">SCHENKEN<br>SIE IHREM<br><b>OBJEKT</b><br>NEUEN<br>GLANZ</div>
  <div class="t center lead">Zuverlässige,<br>professionelle<br>Reinigungskräfte in<br>Paderborn &amp; Gütersloh</div>
  <div class="t center offers-title">UNSERE<br>ANGEBOTE</div>
  <div class="label" style="top:397px;height:22px">Büroreinigung</div>
  <div class="label" style="top:519px;height:22px">Treppenhaus-<br>reinigung</div>
  <div class="label" style="top:650px;height:22px">Bauendreinigung</div>
  <div class="t center cta">Jetzt anrufen<br>0123 9876 543</div>
  <div class="t center web">www.lorvapur.de</div>
</section>

<section class="ad wide" aria-label="Anzeige Querformat">
  <svg class="bg" width="688" height="361" viewBox="0 0 688 361">
    <defs>
      <linearGradient id="photoToneW" x1="0" y1="0" x2="0" y2="1">
        <stop offset="0" stop-color="var(--photo-a)"/>
        <stop offset="1" stop-color="var(--photo-b)"/>
      </linearGradient>
    </defs>
    <rect width="688" height="361" fill="var(--brand-light)"/>
    <polygon points="0,0 268,0 315,324 0,324" fill="var(--white)"/>
    <rect x="0" y="324" width="688" height="37" fill="var(--brand-dark)"/>
    <polygon points="493,324 688,324 688,361 497,361" fill="var(--navy)"/>
    <g stroke="var(--white)" stroke-width="4">
      <polygon points="323,96 435,85 425,277 350,277" fill="url(#photoToneW)" role="img" aria-label="Foto: Reinigungskraft wischt Büroboden"/>
      <polygon points="450,64 523,64 553,240 437,256" fill="url(#photoToneW)" role="img" aria-label="Foto: Putzwagen mit Eimer im Treppenhaus"/>
      <polygon points="537,97 654,86 640,278 565,278" fill="url(#photoToneW)" role="img" aria-label="Foto: Poliermaschine auf glänzendem Boden"/>
    </g>
  </svg>
  <div class="t brand"><i></i>Lorvapur</div>
  <div class="t owner">Inh. Jonas Merbeck</div>
  <div class="t headline">SCHENKEN<br>SIE IHREM <span>OBJEKT</span><br>NEUEN GLANZ</div>
  <div class="rule"></div>
  <div class="t lead">Zuverlässige, professionelle<br>Reinigungskräfte in<br>Paderborn &amp; Gütersloh</div>
  <div class="t center offers-title">Unsere Angebote</div>
  <div class="t center label" style="left:393px;top:284px">Büroreinigung</div>
  <div class="t center label" style="left:493px;top:259px">Treppenhaus-<br>reinigung</div>
  <div class="t center label" style="left:602px;top:284px">Bauendreinigung</div>
  <div class="t band" style="left:22px">Jetzt unverbindliches Angebot einholen</div>
  <div class="t band" style="left:369px">0123 9876 543</div>
  <div class="t band web" style="left:504px">www.lorvapur.de</div>
</section>

</body>
</html>
```